Law Firm Business Card

This is a business card for a law firm that serves US military and veterans.

The card must have ONLY the following (we want an uncluttered look):

- Company logo (PNG, GIF, JPEG copies uploaded)
- A tagline reading: "a law firm for service members and veterans"
- My name and title: "Martin Okello" and "Attorney"
- My email: "martin.okello@harborlinecounsel.com"
- My number: "855-FILE-NOW (345-3669)"

We are looking for a clean, simple layout with only the above information, likely printed on a bright white cotton stock. The font of our logo is DIN 1451, and the font used on our website is Helvetica Neue. The color of our logo is #336699, and we probably want the tagline in that color also, and my contact information in a dark grey. Please review our website at www.harborlinecounsel.com to ensure your card design complements our website style.

Thanks and we look forward to seeing your submissions.

A few notes:

- Two-sided submissions are ok
- Please don't add graphics (scales of justice, judges hammer, etc)

```html
<!DOCTYPE html>
<html lang="en">
<head>
<meta charset="utf-8">
<title>Harborline Counsel — Business Card</title>
<link rel="stylesheet" href="https://fonts.googleapis.com/css2?family=Roboto:wght@300;400&display=swap">
<style>
  :root {
    --brand-blue: #336699;
    --paper-white: #ffffff;
    --ink-grey: #4a4d52;
    --rule-grey: #9a9ea4;
    --backdrop: #d6d8db;
  }
  * { box-sizing: border-box; margin: 0; padding: 0; }
  html, body {
    width: 1200px;
    height: 900px;
    overflow: hidden;
    background: var(--backdrop);
  }
  .canvas {
    position: relative;
    width: 1200px;
    height: 900px;
  }
  .card {
    position: absolute;
    left: 320px;
    width: 560px;
    height: 320px;
    display: flex;
    flex-direction: column;
    align-items: center;
    justify-content: center;
    box-shadow: 0 6px 18px rgba(0, 0, 0, 0.18);
    font-family: "Roboto", "Helvetica Neue", Arial, sans-serif;
  }
  .card--front { top: 110px; background: var(--brand-blue); color: var(--paper-white); }
  .card--back  { top: 470px; background: var(--paper-white); }

  .firm-name {
    display: flex;
    align-items: center;
    gap: 12px;
    font-weight: 400;
    font-size: 36px;
    line-height: 1.1;
  }
  .firm-name__mark {
    width: 18px;
    height: 18px;
    background: currentColor;
    flex: none;
  }
  .card--front .firm-name { color: var(--paper-white); }
  .card--back .firm-name  { color: var(--brand-blue); font-size: 30px; }
  .card--back .firm-name__mark { width: 15px; height: 15px; }

  .tagline {
    margin-top: 20px;
    font-weight: 300;
    font-size: 15px;
    letter-spacing: 1.2px;
  }

  .rule {
    width: 360px;
    height: 1px;
    background: var(--rule-grey);
    margin: 16px 0;
  }
  .person { text-align: center; }
  .person__name  { font-size: 24px; font-weight: 400; color: var(--brand-blue); line-height: 1.1; }
  .person__title { font-size: 13px; font-weight: 300; color: var(--ink-grey); }
  .contact {
    text-align: center;
    font-weight: 300;
    font-size: 15px;
    line-height: 1.35;
    color: var(--ink-grey);
  }
</style>
</head>
<body>
<main class="canvas">
  <section class="card card--front" aria-label="Card front">
    <p class="firm-name"><span class="firm-name__mark"></span>Harborline Counsel</p>
    <p class="tagline">a law firm for service members and veterans</p>
  </section>

  <section class="card card--back" aria-label="Card back">
    <p class="firm-name"><span class="firm-name__mark"></span>Harborline Counsel</p>
    <div class="rule"></div>
    <div class="person">
      <p class="person__name">Martin Okello</p>
      <p class="person__title">Attorney</p>
    </div>
    <div class="rule"></div>
    <div class="contact">
      <p>martin.okello@harborlinecounsel.com</p>
      <p>855-FILE-NOW (345-3669)</p>
    </div>
  </section>
</main>
</body>
</html>
```